Flyer for a marketing

We are a holistic mental health facility in need of a flyer to help promote our services and encourage more people to seek care. See the attachment to tell you more. We prefer warm green colors or rich blue. Thank you.

```html
<!DOCTYPE html>
<html lang="en">
<head>
<meta charset="utf-8">
<title>Willowmere Psychiatric Health and Wellness Flyer</title>
<link href="https://fonts.googleapis.com/css2?family=Montserrat:wght@600;700;800&family=Open+Sans:wght@400;600;700&family=Playfair+Display:wght@700;800&display=swap" rel="stylesheet">
<style>
:root{
  --green:#3d8b3d;
  --green-dark:#1f5a2c;
  --green-deep:#2c6b34;
  --orange:#f2a007;
  --ink:#3b3b3b;
  --page:#eeeeee;
  --paper:#ffffff;
  --photo-a:#c7c4a4;
  --photo-b:#8fa07a;
  --photo-c:#6b8a5a;
}
*{box-sizing:border-box;margin:0;padding:0}
html,body{width:1200px;height:2820px;overflow:hidden;background:var(--page)}
body{position:relative;font-family:"Open Sans",sans-serif;color:var(--ink)}
.flyer{position:absolute;left:50px;top:560px;width:1100px;height:1700px;background:var(--paper);overflow:hidden;box-shadow:0 6px 24px rgba(0,0,0,.12)}
.top-bar{height:50px;background:var(--green);color:#fff;font-weight:700;font-size:18px;letter-spacing:1px;display:flex;align-items:center;justify-content:center}
.hero-photo{position:absolute;left:0;top:50px;width:660px;height:850px;background:linear-gradient(180deg,rgba(255,255,255,0) 75%,#fff 100%),linear-gradient(120deg,var(--photo-a),var(--photo-b) 55%,var(--photo-c))}

.brand{position:absolute;left:730px;top:100px;display:flex;align-items:center;gap:18px}
.brand-square{width:60px;height:60px;background:var(--green)}
.brand-name{font-family:"Playfair Display",serif;font-weight:700;font-size:26px;line-height:1.15;color:var(--green-dark)}
.tagline{position:absolute;left:680px;top:250px;width:400px;text-align:center;font-family:"Playfair Display",serif;font-weight:800;color:var(--green-dark);line-height:1.02}
.tagline .l1{font-size:78px}
.tagline .l2{font-size:72px}
.tagline .small{font-size:46px}
.collage{position:absolute;left:690px;top:500px}
.accept-box{position:absolute;left:740px;top:910px;width:320px;background:var(--green-deep);padding:14px 18px;color:var(--orange);font-weight:700;font-size:23px;line-height:1.2;text-align:right}
.accept-note{position:absolute;left:720px;top:1010px;width:340px;text-align:right;color:var(--green);font-size:17px;line-height:1.4}
.collage-small{position:absolute;left:690px;top:1110px}

.intro{position:absolute;left:50px;top:910px;width:620px;display:flex;flex-direction:column}
.headline{font-family:"Montserrat",sans-serif;font-weight:800;font-size:46px;line-height:1.1;color:var(--green)}
.headline .accent{color:var(--orange)}
.headline .dark{color:var(--green-dark)}
.subhead{margin-top:18px;font-family:"Montserrat",sans-serif;font-weight:700;font-size:31px;line-height:1.2;color:var(--green-dark)}
.why{margin-top:34px;font-family:"Montserrat",sans-serif;font-weight:700;font-size:28px;color:var(--orange)}
.reasons{margin-top:20px;list-style:none}
.reasons li{display:flex;gap:14px;align-items:flex-start;font-size:19px;line-height:1.35;margin-bottom:16px}
.reasons svg{flex:none;margin-top:4px}

.footer{position:absolute;left:0;bottom:0;width:100%;height:110px;background:var(--green);color:#fff;display:flex;align-items:center;padding:0 40px;gap:32px;font-size:16px;line-height:1.45}
.footer .org{font-weight:700}
.footer .addr{width:450px}
.footer .phones{width:230px;border-left:1px solid rgba(255,255,255,.5);padding-left:24px}
.footer .web{border-left:1px solid rgba(255,255,255,.5);padding-left:24px}
</style>
</head>
<body>
<main class="flyer">
  <div class="top-bar">www.willowmerepsychhealth.com</div>
  <div class="hero-photo" role="img" aria-label="Photo of a smiling young woman with curly hair outdoors"></div>

  <div class="brand">
    <span class="brand-square"></span>
    <span class="brand-name">Willowmere<br>Psychiatric<br>Health and<br>Wellness</span>
  </div>

  <h2 class="tagline"><span class="l1">The</span><br><span class="l2">Care <span class="small">You</span></span><br><span class="l2">Deserve</span></h2>

  <svg class="collage" width="390" height="390" viewBox="0 0 390 390" role="img" aria-label="Collage of photos showing an older couple and families enjoying time outdoors">
    <polygon points="195,0 320,90 320,300 195,390 70,300 70,90" fill="#9fb48c"/>
    <polygon points="60,150 120,110 120,250 60,290 0,250 0,150" fill="#b8c7a6"/>
    <polygon points="340,190 390,150 390,300 340,340 300,310 300,220" fill="#7f9b6c"/>
  </svg>

  <div class="accept-box">We are accepting new patients, no waiting list</div>
  <p class="accept-note">Your mental health matters, so make it a priority and call us today for an appointment.</p>

  <svg class="collage-small" width="390" height="350" viewBox="0 0 390 350" role="img" aria-label="Collage of photos showing caring moments between people">
    <polygon points="210,0 295,80 210,160 125,80" fill="#8ea27a"/>
    <polygon points="110,95 190,175 110,255 30,175" fill="#c9b99a"/>
    <polygon points="305,100 385,180 305,260 225,180" fill="#7b9a6a"/>
    <polygon points="210,190 290,270 210,350 130,270" fill="#a8b894"/>
  </svg>

  <section class="intro">
    <h1 class="headline"><span class="dark">WILLOWMERE</span> PSYCHIATRIC HEALTH <span class="dark">AND</span> <span class="accent">WELLNESS,</span></h1>
    <p class="subhead">Where deserving patients meet compassionate providers.</p>
    <h3 class="why">Why choose us?</h3>
    <ul class="reasons">
      <li><svg width="18" height="18" viewBox="0 0 18 18"><path d="M5 2l8 7-8 7" fill="none" stroke="var(--green)" stroke-width="3"/></svg>We are an integrative holistic psychiatric center.</li>
      <li><svg width="18" height="18" viewBox="0 0 18 18"><path d="M5 2l8 7-8 7" fill="none" stroke="var(--green)" stroke-width="3"/></svg>Our mission is to provide compassionate quality care.</li>
      <li><svg width="18" height="18" viewBox="0 0 18 18"><path d="M5 2l8 7-8 7" fill="none" stroke="var(--green)" stroke-width="3"/></svg>We provide psychiatric services including medication management and psychotherapy.</li>
      <li><svg width="18" height="18" viewBox="0 0 18 18"><path d="M5 2l8 7-8 7" fill="none" stroke="var(--green)" stroke-width="3"/></svg>We listen, care, and empower you to live better.</li>
      <li><svg width="18" height="18" viewBox="0 0 18 18"><path d="M5 2l8 7-8 7" fill="none" stroke="var(--green)" stroke-width="3"/></svg>We accept major insurances.</li>
    </ul>
  </section>

  <footer class="footer">
    <div class="addr"><span class="org">Willowmere Psychiatric Health and Wellness, APNC</span><br>4810 Cedar Hollow Road, Suite 120 Fairview, CA 90000</div>
    <div class="phones">Ph (555) 214-0187<br>Fax (555) 214-0199</div>
    <div class="web">info@willowmerepsychhealth.com<br>willowmerepsychhealth.com</div>
  </footer>
</main>
</body>
</html>
```